Web Design Project

I need a website for a motorcycle sales business I have started.
I specialise in sourcing and importing older Corvane Tellmores.
I sell them or restore them pending on their condition. I could have up to 5-15 bikes at any one time for sale. I also sell secondhand spare parts.
I want to be able to upload pics and text for each bike, so I guess I may need a page for each bike with up to 10 medium resolution pics per page and a text box for around 100-200 words as well.
Ideally have a look at the Corvane Tellmore website.
I would like my site to be sophisticated but simple, understated but tough.
My colors are black and orange.

Target Market(s)

mostly guys aged from early 30's to 60's

Industry/Entity Type

Business

Requirements
Nice to have
• Pics that fade on the home page?
darker background?

```html
<!DOCTYPE html>
<html lang="en">
<head>
<meta charset="utf-8">
<title>Ironvale Road Motorcycles</title>
<link rel="stylesheet" href="https://fonts.googleapis.com/css2?family=PT+Sans:ital,wght@0,400;0,700;1,400;1,700&family=Roboto+Condensed:wght@500&family=Arimo:ital,wght@0,400;1,400&display=swap">
<style>
:root{
  --bg:#14100c;
  --bg-warm:#2a1f14;
  --panel:#1b1b1b;
  --panel-top:#2a2a2a;
  --orange:#f0a21a;
  --orange-dark:#d7830a;
  --orange-light:#ffc94a;
  --text:#ffffff;
  --muted:#a9a9a9;
  --strip:#ececec;
  --dark-text:#222;
}
*{box-sizing:border-box;margin:0;padding:0}
html,body{width:942px;height:1200px;overflow:hidden}
body{position:relative;background:radial-gradient(ellipse at 50% 20%,var(--bg-warm),var(--bg) 70%);font-family:"Arimo",Arial,sans-serif;color:var(--text)}
.abs{position:absolute}

.utility{top:9px;left:579px;font-size:12px;color:#eee;display:flex;align-items:center;gap:6px}
.utility .sep{color:#999}
.utility .connect{margin-left:14px;margin-right:2px}
.utility .dot{width:19px;height:19px;border-radius:50%;background:#8a9bb5}
.utility .dot.orange{background:#d9782a}
.header-line{top:31px;left:0;width:942px;height:1px;background:#3a3128}

.bike-art{top:12px;left:38px;width:140px;height:130px;border-radius:50% 40% 50% 50%;background:radial-gradient(circle at 60% 65%,#cfd3d8,#3d5da8 45%,#181818 80%);opacity:.9}
.brand{top:40px;left:175px;font-family:"PT Sans",sans-serif;font-weight:700;font-size:30px;line-height:31px;color:#f2f2f2}
.brand span{display:block;padding-left:108px}
.phone{top:61px;left:726px;display:flex;align-items:center;gap:8px;font-family:"PT Sans",sans-serif;font-style:italic;font-weight:700;font-size:22px;color:#eee}
.phone .icon{width:31px;height:31px;background:#fff;border-radius:5px;display:flex;align-items:center;justify-content:center}

.nav{top:108px;left:0;width:942px;height:34px;background:linear-gradient(var(--orange-light),var(--orange) 50%,var(--orange-dark))}
.nav ul{list-style:none;display:flex;height:100%;align-items:center;font-family:"Roboto Condensed",sans-serif;font-weight:500;font-size:16px;color:#1a1a1a}
.nav li{margin-left:24px}
.nav .home{margin-left:0;width:288px;height:34px;display:flex;align-items:center;justify-content:center;padding-left:185px;color:#fff;background:linear-gradient(100deg,transparent 188px,#7a7a7a 189px,#3d3d3d 275px,transparent 276px)}

.hero{top:152px;left:37px;width:868px;height:475px;border-radius:4px;overflow:hidden}
.hero-photo{position:absolute;inset:0;background:linear-gradient(180deg,#3b4656 0%,#2a3340 40%,#6e6f6c 72%,#8a8a86 100%)}
.slides{position:absolute;top:24px;right:17px;display:flex;gap:6px}
.slides i{width:18px;height:13px;border-radius:3px;background:#8a6012}
.slides i.on{background:var(--orange)}
.welcome{position:absolute;left:0;bottom:0;width:868px;height:102px;background:linear-gradient(#fafafa,var(--strip) 60%,#cfcfcf)}
.welcome svg{position:absolute;left:288px;top:0}
.welcome h1{position:absolute;left:16px;top:6px;font-family:"PT Sans",sans-serif;font-weight:700;font-style:italic;font-size:32px;line-height:30px;color:var(--dark-text)}
.welcome h1 em{font-style:italic;color:var(--orange-dark);font-size:36px}
.welcome h1 .l2{display:block;font-size:24px;padding-left:32px;line-height:27px}
.welcome h1 .l3{display:block;font-size:24px;padding-left:140px;line-height:25px}
.welcome p{position:absolute;left:397px;top:10px;width:458px;font-style:italic;font-size:12.5px;line-height:17px;color:#333;text-align:justify}

.btn{display:inline-block;background:linear-gradient(var(--orange-light),var(--orange-dark));color:#1a1a1a;font-family:"PT Sans",sans-serif;font-weight:700;font-size:15px;padding:5px 9px;border-radius:4px;transform:skewX(-8deg)}
.welcome .btn{position:absolute;left:640px;top:66px}

.card{top:651px;width:277px;height:306px;border-radius:4px;background:linear-gradient(var(--panel-top),var(--panel) 30%,#141414);padding:12px 18px}
.card h2{font-family:"PT Sans",sans-serif;font-style:italic;font-weight:400;font-size:21px;line-height:24px;color:#fff}
.card h2 b{display:block;color:var(--orange);font-weight:700;font-size:25px;line-height:28px;font-style:normal}
.thumb{margin-top:12px;width:242px;height:108px;border:2px solid #ddd}
.card p{font-style:italic;font-size:12px;line-height:17px;color:var(--muted);margin-top:12px;text-align:justify}
.card .foot{position:absolute;bottom:6px;left:0;right:0;display:flex;justify-content:center}
.news h3{font-family:"PT Sans",sans-serif;font-weight:700;font-size:13px;line-height:14px;text-decoration:underline;margin-top:16px;text-align:justify}
.news p{margin-top:6px}
.more{display:block;text-align:right;font-family:"PT Sans",sans-serif;font-style:italic;font-weight:700;font-size:13px;color:var(--orange);margin-top:9px}
.news hr{border:0;border-top:1px solid #555;margin-top:8px}
.offer .foot{justify-content:space-between;padding:0 20px;align-items:center}
.price{font-family:"PT Sans",sans-serif;font-style:italic;font-size:20px;color:#eee}

.info{top:970px;left:37px;width:868px;height:192px;border-radius:4px;background:linear-gradient(#262626,#1a1a1a)}
.info h2{position:absolute;font-family:"PT Sans",sans-serif;font-style:italic;font-weight:400;font-size:23px;color:#e8e8e8}
.contact{position:absolute;left:20px;top:47px;font-size:12px;line-height:15px;color:#cfcfcf}
.contact dt{color:var(--orange);margin-top:4px}
.contact dd{margin-bottom:2px}
.map{position:absolute;left:202px;top:41px;width:246px;height:136px;background:linear-gradient(135deg,#d9d4c2,#bcc9d6 60%,#a9bccd)}
.portrait{position:absolute;left:515px;top:50px;width:134px;height:116px;background:#ddd;border:3px solid #fff;transform:rotate(-3deg)}
.testimonial{position:absolute;left:665px;top:50px;width:190px}
.testimonial h3{font-family:"PT Sans",sans-serif;font-weight:700;font-size:13px;line-height:14px;text-decoration:underline;text-align:justify}
.testimonial p{font-style:italic;font-size:12px;line-height:16px;color:var(--muted);margin-top:6px}
.testimonial .by{display:flex;justify-content:space-between;margin-top:14px;font-family:"PT Sans",sans-serif;font-style:italic;font-weight:700;font-size:12px}
.testimonial .by a{color:var(--orange)}

.footer{top:1173px;left:0;width:942px;text-align:center;font-size:12px;color:#ccc}
</style>
</head>
<body>
<div class="abs utility">
  <span>Login</span><span class="sep">|</span><span>Pricing</span><span class="sep">|</span><span>Sitemap</span>
  <span class="connect">Connect with us on:</span>
  <span class="dot"></span><span class="dot"></span><span class="dot orange"></span>
</div>
<div class="abs header-line"></div>

<div class="abs bike-art" role="img" aria-label="Chrome custom motorcycle illustration"></div>
<div class="abs brand">Ironvale Road<span>Motorcycles</span></div>
<div class="abs phone">
  <span class="icon"><svg width="18" height="22" viewBox="0 0 18 22"><path d="M4 1h4l1 5-3 2c1 3 3 6 6 8l2-3 4 2v4c0 2-2 3-4 2C7 18 2 11 1 5 1 3 2 1 4 1z" fill="#222"/></svg></span>
  020 4821 0937
</div>

<nav class="abs nav">
  <ul>
    <li class="home">HOME</li><li>WHO WE ARE</li><li>WHAT WE DO</li><li>NEW ARRIVALS</li><li>ACCESSORIES</li><li>NEWS &amp; EVENTS</li><li>FIND US</li>
  </ul>
</nav>

<section class="abs hero">
  <div class="hero-photo" role="img" aria-label="Classic black and orange touring motorcycle parked outside a workshop"></div>
  <div class="slides"><i class="on"></i><i></i><i></i><i></i></div>
  <div class="welcome">
    <svg width="100" height="102" viewBox="0 0 100 102"><path d="M38 0h22l38 51-38 51H38l38-51z" fill="#f0a21a"/><path d="M38 0h22l38 51H76z" fill="#ffc94a"/></svg>
    <h1><em>W</em>elcome to<span class="l2">Ironvale Road</span><span class="l3">Motorcycles</span></h1>
    <p>Lorem ipsum dolor sit amet, consec tetuer adipiscing elit. Praesent vestibulum moles tie lacus. Aenean nonummy hendrerit mauris. Phasellus porta. Fusce suscipit varius mi. Cum sociis natoque penatibus et magnis dis parturient montes, nascetur ridiculus mus. Nulla dui.</p>
    <span class="btn">READ MORE</span>
  </div>
</section>

<article class="abs card" style="left:37px">
  <h2>New<b>Arrivals Bike</b></h2>
  <div class="thumb" role="img" aria-label="Blue custom motorcycle" style="background:linear-gradient(135deg,#c9c9c9,#2e4b9a 55%,#222)"></div>
  <p>Lorem ipsum dolor sit amet, consec tetuer adipiscing elit. Praesent vestibulum moles tie lacus. Aenean nonummy hendrerit mauris. Phasellus porta. Fusce suscipit varius mi.</p>
  <div class="foot"><span class="btn">READ MORE</span></div>
</article>

<article class="abs card news" style="left:333px">
  <h2>Latest<b>News &amp; Events</b></h2>
  <h3>Corvane Tellmore Recall</h3>
  <p>Lorem ipsum dolor sit amet, consec tetuer adipiscing elit. Praesent vestibulum moles tie lacus.</p>
  <a class="more">Continue..</a>
  <hr>
  <h3>2012 Corvane Tellmores available for Import</h3>
  <p>Lorem ipsum dolor sit amet, consec tetuer adipiscing elit. Praesent vestibulum moles tie lacus.</p>
  <a class="more">Continue..</a>
</article>

<article class="abs card offer" style="left:628px">
  <h2>Special<b>Offers on Bikes</b></h2>
  <div class="thumb" role="img" aria-label="Black classic motorcycle in a garden" style="background:linear-gradient(135deg,#6f7d5a,#2b2b2b 55%,#9a9a9a)"></div>
  <p>Lorem ipsum dolor sit amet, consec tetuer adipiscing elit. Praesent vestibulum moles tie lacus.</p>
  <div class="foot"><span class="price">ONLY $ 19999</span><span class="btn">BUY NOW !</span></div>
</article>

<section class="abs info">
  <h2 style="left:20px;top:12px">Our Location</h2>
  <dl class="contact">
    <dt>// Adderss:</dt><dd>Lorem ipsum dolor<br>Street No. 123</dd>
    <dt>// Phone:</dt><dd>020 4821 0937</dd>
    <dt>// Email ID :</dt><dd>info@ironvaleroadmotors.com</dd>
  </dl>
  <div class="map" role="img" aria-label="Street map showing the showroom location"></div>
  <h2 style="left:517px;top:12px">Client Testimonials</h2>
  <div class="portrait" role="img" aria-label="Customer portrait placeholder"></div>
  <div class="testimonial">
    <h3>2012 Corvane Tellmores available for Import</h3>
    <p>Lorem ipsum dolor sit amet, consec tetuer adipiscing elit. Praesent vestibulum moles tie lacus.</p>
    <div class="by"><span>By Mark Delaney</span><a>Continue..</a></div>
  </div>
</section>

<footer class="abs footer">Copyright © 2012 &nbsp;Ironvale Road Motorcycles &nbsp;/ &nbsp;Call : &nbsp;020 4821 0937</footer>
</body>
</html>
```